Stroomwacht Powerpoint - presentation slides for energy management tool

We need a Powerpoint presentation lay-out which matches our logo from Stroomwacht.nl. 10 slides variations minimum, enough for a full professional presentation to potential clients.
Stroomwacht is a Dutch energymanagement tool for corporate real estate and housing agency. Our clients are Social houseing organisation, real estate owers, property managers and property developers.
Target Market(s)
real estate owners
Property manage
Font styles to use
Sans Serif
Colors
f78f20
0255a3
Requirements
Must have
- Stroomwacht logo colors and style
#F37122 orange
#00345D darkblue
Nice to have
- Professional look, background not white in every slide
Should not have
- wrong color orange and blue.

```html
<!DOCTYPE html>
<html lang="en">
<head>
<meta charset="utf-8">
<title>Stroomwacht – presentation slide set</title>
<link href="https://fonts.googleapis.com/css2?family=Oswald:wght@400;500&family=Open+Sans:wght@400;600;700&display=swap" rel="stylesheet">
<style>
:root{
  --orange:#F37122;
  --amber:#f78f20;
  --navy:#00345D;
  --blue:#0255a3;
  --sky:#3f6fc4;
  --gold:#f4b71c;
  --grey:#8b8b8b;
  --ink:#3a3a3a;
  --paper:#ffffff;
  --rule:#dcdcdc;
}
*{box-sizing:border-box;margin:0;padding:0}
html,body{width:714px;height:1200px;overflow:hidden;background:var(--paper)}
body{position:relative;font-family:'Open Sans',sans-serif;color:var(--ink)}
.slide{position:absolute;width:222px;height:125px;overflow:hidden;background:var(--paper);box-shadow:0 2px 6px rgba(0,0,0,.35)}
.abs{position:absolute}
.title{position:absolute;font-family:'Oswald',sans-serif;font-weight:400;text-transform:uppercase;color:var(--navy);line-height:1.1;white-space:nowrap}
.title .hl{color:var(--orange)}
.on-dark{color:var(--paper)}
.copy{position:absolute;font-size:4px;line-height:1.35;color:var(--ink)}
.copy b{font-weight:700;display:block}
.copy.light{color:var(--paper)}
.brand{position:absolute;display:flex;align-items:center;gap:2px;font-family:'Oswald',sans-serif;font-weight:500;color:var(--navy);font-size:5.5px;white-space:nowrap}
.brand::before{content:"";width:1em;height:1em;border-radius:50%;background:var(--orange);flex:none}
.brand.light{color:var(--paper)}
.ticks{position:absolute;right:5px;top:14px;bottom:14px;width:2px;background:repeating-linear-gradient(var(--grey) 0 1px,transparent 1px 4px);opacity:.6}
.ticks.light{background:repeating-linear-gradient(rgba(255,255,255,.8) 0 1px,transparent 1px 4px)}
.bar-navy{position:absolute;left:0;right:0;bottom:0;height:4px;background:var(--navy)}
.bar-orange{position:absolute;left:0;right:0;bottom:0;height:3px;background:var(--orange)}
.photo{position:absolute}
.photo-city-night{background:linear-gradient(160deg,#1d3a5c,#0d2440 55%,#24324a)}
.photo-city-warm{background:linear-gradient(160deg,#b99b78,#6f6b6e 50%,#3c4a5e)}
.photo-city-day{background:linear-gradient(170deg,#8fa8c4,#5a6f86 55%,#3b4656)}
.photo-lights{background:linear-gradient(170deg,#2d2a30,#7a5a34 55%,#1d2636)}
.ring{position:absolute;border-radius:50%;display:flex;align-items:center;justify-content:center}
.ring svg{width:55%;height:55%}
.label{position:absolute;font-size:4px;font-weight:600;text-align:center;line-height:1.2}
.num{position:absolute;width:9px;height:9px;font-family:'Oswald',sans-serif;font-size:6px;display:flex;align-items:center;justify-content:center}
.num.fill{background:var(--orange);color:var(--paper)}
.num.line{border:.8px solid var(--paper);color:var(--paper)}
.num-label{position:absolute;font-size:3.5px;line-height:1.2;color:var(--paper);width:18px}
table.grid{position:absolute;border-collapse:collapse;font-size:3px;text-align:center}
table.grid td,table.grid th{border:.5px solid var(--rule);height:7px;width:28px;font-weight:400}
table.grid th{color:var(--paper);font-weight:600}
table.grid .price td{height:14px;color:var(--paper);font-size:5px;font-family:'Oswald',sans-serif;border-color:var(--paper)}
.device{position:absolute;background:#eeeeee;border:3px solid #2b2b2b;border-radius:4px}
.icon-dot{position:absolute;width:9px;height:9px;border-radius:50%;background:var(--navy);display:flex;align-items:center;justify-content:center}
.icon-dot svg{width:60%;height:60%}
.tiny{position:absolute;font-size:3.5px;color:var(--ink);white-space:nowrap}
</style>
</head>
<body>

<svg width="0" height="0" style="position:absolute" aria-hidden="true">
  <defs>
    <symbol id="i-search" viewBox="0 0 24 24"><circle cx="10" cy="10" r="6" fill="none" stroke="currentColor" stroke-width="2.5"/><path d="M14.5 14.5 21 21" stroke="currentColor" stroke-width="3" stroke-linecap="round"/></symbol>
    <symbol id="i-gear" viewBox="0 0 24 24"><circle cx="12" cy="12" r="6.5" fill="none" stroke="currentColor" stroke-width="3" stroke-dasharray="3 2"/><circle cx="12" cy="12" r="3" fill="currentColor"/></symbol>
    <symbol id="i-eye" viewBox="0 0 24 24"><path d="M2 12Q12 2 22 12Q12 22 2 12Z" fill="none" stroke="currentColor" stroke-width="2"/><circle cx="12" cy="12" r="3.5" fill="currentColor"/></symbol>
    <symbol id="i-home" viewBox="0 0 24 24"><path d="M3 12 12 4l9 8h-3v8h-5v-5h-2v5H6v-8Z" fill="currentColor"/></symbol>
    <symbol id="i-doc" viewBox="0 0 24 24"><rect x="5" y="3" width="14" height="18" rx="1" fill="currentColor"/><path d="M8 8h8M8 12h8M8 16h5" stroke="#fff" stroke-width="1.5"/></symbol>
    <symbol id="i-globe" viewBox="0 0 24 24"><circle cx="12" cy="12" r="9" fill="none" stroke="currentColor" stroke-width="2"/><ellipse cx="12" cy="12" rx="4" ry="9" fill="none" stroke="currentColor" stroke-width="1.5"/><path d="M3 12h18" stroke="currentColor" stroke-width="1.5"/></symbol>
    <symbol id="i-bolt" viewBox="0 0 24 24"><path d="M13 2 5 14h6l-2 8 9-12h-6Z" fill="currentColor"/></symbol>
  </defs>
</svg>

<!-- Row 1 -->
<section class="slide photo-city-night" style="left:1px;top:42px" role="img" aria-label="Title slide over a night city photograph">
  <div class="brand light" style="left:30px;top:44px;font-size:15px">Stroomwacht</div>
  <div class="title on-dark" style="left:34px;top:72px;font-size:7.5px">Your awesome title here</div>
</section>

<section class="slide" style="left:247px;top:42px;background:var(--navy)">
  <svg class="abs" width="222" height="125" viewBox="0 0 222 125" role="img" aria-label="Orange band with city photograph below a curved edge">
    <path d="M0 78Q40 40 110 52T222 30V125H0Z" fill="var(--orange)"/>
    <path d="M0 78Q40 40 110 52T222 30" fill="none" stroke="var(--paper)" stroke-width="1.5"/>
  </svg>
  <div class="brand light" style="left:68px;top:14px;font-size:13px">Stroomwacht</div>
  <div class="title on-dark" style="left:0;right:0;top:83px;font-size:8px;text-align:center">Your awesome title here</div>
  <div class="tiny" style="left:0;right:0;bottom:4px;text-align:center;color:var(--paper);opacity:.7">w w w . s t r o o m w a c h t . n l</div>
  <div class="ticks light"></div>
</section>

<section class="slide photo" style="left:491px;top:42px;background:linear-gradient(170deg,#eef1f5,#e6dccc 55%,#d8cbb6)" role="img" aria-label="Faded city photograph background">
  <div class="brand" style="left:88px;top:16px;font-size:9px">Stroomwacht</div>
  <div class="title" style="left:0;right:0;top:56px;font-size:8px;text-align:center;color:var(--orange)">Your awesome title here</div>
  <div class="title" style="left:0;right:0;top:68px;font-size:5px;text-align:center;color:var(--orange)">And subtitle</div>
</section>

<!-- Row 2 -->
<section class="slide photo-city-night" style="left:1px;top:190px">
  <div class="brand light" style="right:6px;top:6px">Stroomwacht</div>
  <div class="title on-dark" style="left:12px;top:60px;font-size:8.5px">Numbered <span class="hl">slides</span></div>
  <div class="copy light" style="left:12px;top:74px;width:95px">Why choose us?<br>Clear insight into energy use across every building, shown in simple monthly reports for each portfolio.</div>
  <div class="num fill" style="left:125px;top:36px">1</div><div class="num-label" style="left:137px;top:37px">What is energy data?</div>
  <div class="num line" style="left:167px;top:36px">2</div><div class="num-label" style="left:179px;top:37px">What is a smart meter?</div>
  <div class="num fill" style="left:125px;top:61px">3</div><div class="num-label" style="left:137px;top:62px">What is a usage report?</div>
  <div class="num line" style="left:167px;top:61px">4</div><div class="num-label" style="left:179px;top:62px">What is a target?</div>
  <div class="num fill" style="left:125px;top:86px">5</div><div class="num-label" style="left:137px;top:87px">What is a saving?</div>
  <div class="num line" style="left:167px;top:86px">6</div><div class="num-label" style="left:179px;top:87px">What is a portfolio?</div>
  <div class="bar-orange"></div>
</section>

<section class="slide" style="left:247px;top:190px">
  <div class="title" style="left:0;right:0;top:10px;font-size:8px;text-align:center;color:var(--orange)">Wellcome message</div>
  <div class="copy" style="left:12px;top:38px;width:195px"><b>What is Stroomwacht?</b>Stroomwacht is an energy management tool for housing associations and real estate owners. It collects meter readings from every building, compares use month by month and points out where savings can be made. Property managers see their whole portfolio in one clear view and act on the figures that matter most.</div>
  <div class="photo" style="left:98px;top:88px;width:124px;height:33px;background:linear-gradient(180deg,rgba(0,52,93,.2),var(--navy))" role="img" aria-label="City skyline silhouette"></div>
  <div class="bar-navy"></div>
  <div class="brand" style="left:14px;bottom:8px">Stroomwacht</div>
  <div class="ticks"></div>
</section>

<section class="slide" style="left:491px;top:190px;background:var(--navy)">
  <div class="abs" style="left:10px;top:0;width:52px;height:125px;background:var(--orange)"></div>
  <div class="photo" style="left:24px;top:34px;width:64px;height:58px;background:linear-gradient(160deg,#c9c3bd,#8e8780);border:2px solid var(--paper)" role="img" aria-label="Portrait photograph of a team member"></div>
  <div class="brand light" style="right:6px;top:6px">Stroomwacht</div>
  <div class="title on-dark" style="left:120px;top:40px;font-size:8px">Something <span class="hl">about us</span></div>
  <div class="copy light" style="left:120px;top:56px;width:92px">Why do we use it?<br>We help owners lower energy costs with clear data, friendly support and honest advice for every site.</div>
  <div class="copy light" style="left:120px;top:88px">Piet Jansen</div>
  <div class="bar-orange"></div>
</section>

<!-- Row 3 -->
<section class="slide" style="left:1px;top:362px">
  <div class="photo photo-city-day" style="left:0;top:0;width:100px;height:125px;clip-path:polygon(0 0,100% 0,55% 100%,0 100%)" role="img" aria-label="Daytime city photograph with tower"></div>
  <div class="title" style="left:125px;top:14px;font-size:8px">Wellcome <span class="hl">message</span></div>
  <div class="copy" style="left:125px;top:27px;width:85px">What is Stroomwacht?<br>Stroomwacht is an energy management tool for corporate real estate. It reads every meter, stores the data safely and shows trends for each building. Managers compare sites, set targets and follow savings over time. Reports are ready each month and can be shared with owners, tenants and advisors without extra work or cost.</div>
  <div class="brand" style="right:12px;bottom:6px">Stroomwacht</div>
  <div class="ticks"></div>
</section>

<section class="slide" style="left:247px;top:338px">
  <div class="abs" style="left:0;top:0;width:58px;height:125px;background:var(--orange)"></div>
  <div class="photo photo-lights" style="left:18px;top:20px;width:74px;height:74px;border-radius:50%;border:3px solid var(--paper)" role="img" aria-label="Round photograph of a city street at dusk"></div>
  <div class="title" style="left:90px;top:32px;font-size:7.5px;color:var(--orange)">Something <span style="color:var(--navy)">about mission</span></div>
  <div class="copy" style="left:90px;top:45px;width:118px">What is our mission?<br>We want every building to use less energy. Our tool turns raw meter readings into clear advice, so owners and managers know where to act first and can prove the results to their tenants and boards.</div>
  <div class="bar-navy"></div>
  <div class="brand" style="right:12px;bottom:7px">Stroomwacht</div>
  <div class="ticks"></div>
</section>

<section class="slide" style="left:491px;top:362px">
  <div class="title" style="left:12px;top:8px;font-size:8px">Our <span class="hl">vision</span></div>
  <div class="brand" style="right:6px;top:6px">Stroomwacht</div>
  <div class="photo photo-lights" style="left:0;top:24px;width:222px;height:62px" role="img" aria-label="Aerial photograph of a city at night"></div>
  <div class="copy" style="left:12px;top:92px;width:200px">What is our vision?<br>Smart energy data for every property, so owners save money and lower their footprint year after year.</div>
  <div class="bar-navy"></div>
</section>

<!-- Row 4 -->
<section class="slide" style="left:1px;top:522px;background:var(--navy)">
  <div class="photo" style="left:80px;top:60px;width:142px;height:62px;background:linear-gradient(180deg,rgba(255,255,255,0),rgba(255,255,255,.12))" role="img" aria-label="Faint city skyline"></div>
  <div class="title on-dark" style="left:12px;top:12px;font-size:8px">What we <span class="hl">do</span></div>
  <div class="brand light" style="right:6px;top:6px">Stroomwacht</div>
  <div class="ring" style="left:92px;top:16px;width:20px;height:20px;border:1px solid var(--orange);color:var(--orange)"><svg><use href="#i-search"/></svg></div>
  <div class="label" style="left:80px;top:40px;width:44px;color:var(--paper)">Where does it come from?</div>
  <div class="ring" style="left:30px;top:62px;width:20px;height:20px;border:1px solid var(--orange);color:var(--orange)"><svg><use href="#i-gear"/></svg></div>
  <div class="label" style="left:18px;top:86px;width:44px;color:var(--paper)">Where can I get some?</div>
  <div class="ring" style="left:155px;top:62px;width:20px;height:20px;border:1px solid var(--orange);color:var(--orange)"><svg><use href="#i-eye"/></svg></div>
  <div class="label" style="left:143px;top:86px;width:44px;color:var(--paper)">Where can I get some?</div>
  <div class="bar-orange"></div>
</section>

<section class="slide" style="left:247px;top:485px;background:var(--navy)">
  <div class="abs" style="left:0;top:0;width:222px;height:52px;background:var(--orange)"></div>
  <div class="title on-dark" style="left:0;right:0;top:10px;font-size:8px;text-align:center">What we do</div>
  <div class="photo photo-city-day" style="left:15px;top:30px;width:44px;height:38px;border:2px solid var(--paper)" role="img" aria-label="Photograph of an office building entrance"></div>
  <div class="photo photo-city-warm" style="left:89px;top:30px;width:44px;height:38px;border:2px solid var(--paper)" role="img" aria-label="Photograph of a city street"></div>
  <div class="photo photo-city-day" style="left:163px;top:30px;width:44px;height:38px;border:2px solid var(--paper)" role="img" aria-label="Photograph of a modern interior"></div>
  <div class="label" style="left:10px;top:74px;width:54px;color:var(--paper)">Where can I get some?</div>
  <div class="label" style="left:84px;top:74px;width:54px;color:var(--paper)">Where does it come from?</div>
  <div class="label" style="left:158px;top:74px;width:54px;color:var(--paper)">Where can I get some?</div>
  <div class="copy light" style="left:10px;top:88px;width:54px;text-align:center;font-size:3.2px">Live meter data for every site, updated each hour.</div>
  <div class="copy light" style="left:84px;top:88px;width:54px;text-align:center;font-size:3.2px">Monthly reports that owners and tenants understand.</div>
  <div class="copy light" style="left:158px;top:88px;width:54px;text-align:center;font-size:3.2px">Clear advice on where to save energy first.</div>
  <div class="ticks light"></div>
</section>

<section class="slide photo-city-night" style="left:491px;top:522px" role="img" aria-label="Night city photograph background">
  <div class="title on-dark" style="left:12px;top:12px;font-size:8px">Description</div>
  <div class="brand light" style="right:6px;top:6px">Stroomwacht</div>
  <div class="ring" style="left:14px;top:36px;width:36px;height:36px;background:var(--navy);border:1.5px solid var(--paper);color:var(--paper)"><svg><use href="#i-gear"/></svg></div>
  <div class="ring" style="left:93px;top:36px;width:36px;height:36px;background:var(--navy);border:1.5px solid var(--paper);color:var(--paper)"><svg><use href="#i-search"/></svg></div>
  <div class="ring" style="left:172px;top:36px;width:36px;height:36px;background:var(--navy);border:1.5px solid var(--paper);color:var(--paper)"><svg><use href="#i-eye"/></svg></div>
  <div class="label" style="left:4px;top:78px;width:56px;color:var(--paper)">Where can I get some?</div>
  <div class="label" style="left:83px;top:78px;width:56px;color:var(--paper)">Where does it come from?</div>
  <div class="label" style="left:162px;top:78px;width:56px;color:var(--paper)">Where can I get some?</div>
  <div class="copy light" style="left:4px;top:90px;width:56px;text-align:center;font-size:3.2px">Meter data from all buildings in one place.</div>
  <div class="copy light" style="left:83px;top:90px;width:56px;text-align:center;font-size:3.2px">Trends and alerts when usage rises.</div>
  <div class="copy light" style="left:162px;top:90px;width:56px;text-align:center;font-size:3.2px">Reports ready to share with clients.</div>
  <div class="bar-orange"></div>
</section>

<!-- Row 5 -->
<section class="slide" style="left:1px;top:685px">
  <div class="title" style="left:12px;top:12px;font-size:8px">Full text <span class="hl">slide</span></div>
  <div class="brand" style="right:6px;top:6px">Stroomwacht</div>
  <div class="copy" style="left:12px;top:28px;width:198px">What is Stroomwacht?<br>Stroomwacht is an energy management tool for housing associations, property managers and developers. It reads gas, power and water meters, checks the data and shows the results per building, per month and per year. Users set targets, compare sites and receive alerts when use rises.</div>
  <div class="copy" style="left:12px;top:70px;width:198px">Why use it?<br>Energy is one of the largest costs in any portfolio. With clear figures owners can plan upgrades, talk with tenants and prove the savings they make. Reports are ready each month without extra work.</div>
  <div class="bar-navy"></div>
  <div class="ticks"></div>
</section>

<section class="slide" style="left:247px;top:633px">
  <div class="photo photo-city-day" style="left:112px;top:0;width:110px;height:122px" role="img" aria-label="Photograph of a city skyline"></div>
  <div class="title" style="left:12px;top:34px;font-size:8px">2 collumn <span class="hl">text</span></div>
  <div class="copy" style="left:12px;top:48px;width:92px">Why do we use it?<br>Clear data helps every owner see where energy goes and how to cut waste in each building.</div>
  <div class="copy light" style="left:120px;top:48px;width:92px">Why do we use it?<br>Our reports turn meter readings into simple steps that teams can plan, follow and measure.</div>
  <div class="bar-orange"></div>
</section>

<section class="slide" style="left:491px;top:681px">
  <div class="abs" style="left:0;top:0;width:112px;height:125px;background:var(--navy)"></div>
  <div class="photo" style="left:0;top:70px;width:112px;height:52px;background:linear-gradient(180deg,rgba(255,255,255,0),rgba(255,255,255,.12))" role="img" aria-label="Faint city skyline"></div>
  <div class="title on-dark" style="left:10px;top:12px;font-size:8px">Achivements <span class="hl">text</span></div>
  <div class="brand" style="right:6px;top:6px">Stroomwacht</div>
  <div class="icon-dot" style="left:108px;top:16px;color:var(--paper)"><svg><use href="#i-search"/></svg></div>
  <div class="icon-dot" style="left:108px;top:32px;color:var(--paper)"><svg><use href="#i-gear"/></svg></div>
  <div class="icon-dot" style="left:108px;top:48px;color:var(--paper)"><svg><use href="#i-eye"/></svg></div>
  <div class="icon-dot" style="left:108px;top:64px;color:var(--paper)"><svg><use href="#i-search"/></svg></div>
  <div class="icon-dot" style="left:108px;top:80px;color:var(--paper)"><svg><use href="#i-gear"/></svg></div>
  <div class="icon-dot" style="left:108px;top:96px;color:var(--paper)"><svg><use href="#i-eye"/></svg></div>
  <div class="copy" style="left:124px;top:16px;width:90px;line-height:1.25">What is a saving?<br><b>1,200 homes</b>connected in year one</div>
  <div class="copy" style="left:124px;top:48px;width:90px;line-height:1.25">What is a saving?<br><b>18% less energy</b>across all sites</div>
  <div class="copy" style="left:124px;top:80px;width:90px;line-height:1.25">What is a saving?<br><b>40 clients</b>in the Netherlands</div>
  <div class="bar-orange"></div>
</section>

<!-- Row 6 -->
<section class="slide" style="left:247px;top:779px">
  <div class="title" style="left:0;right:0;top:8px;font-size:8px;text-align:center">Table <span class="hl">name</span></div>
  <table class="grid" style="left:12px;top:24px">
    <tr>
      <th style="background:var(--sky)">Site</th><th style="background:var(--sky)">Gas</th><th style="background:var(--orange)">Power</th><th style="background:var(--sky)">Water</th><th style="background:var(--sky)">Heat</th><th style="background:var(--orange)">Solar</th><th style="background:var(--sky)">Total</th>
    </tr>
    <tr><td>North</td><td>Text</td><td>Text</td><td>Text</td><td>Text</td><td>Text</td><td>Text</td></tr>
    <tr><td>South</td><td>Text</td><td>Text</td><td>Text</td><td>Text</td><td>Text</td><td>Text</td></tr>
    <tr><td>East</td><td>Text</td><td>Text</td><td>Text</td><td>Text</td><td>Text</td><td>Text</td></tr>
    <tr><td>West</td><td>Text</td><td>Text</td><td>Text</td><td>Text</td><td>Text</td><td>Text</td></tr>
    <tr><td>Centre</td><td>Text</td><td>Text</td><td>Text</td><td>Text</td><td>Text</td><td>Text</td></tr>
    <tr class="price">
      <td style="background:var(--sky)">$35</td><td style="background:var(--orange)">$40</td><td style="background:var(--sky)">$35</td><td style="background:var(--orange)">$25</td><td style="background:var(--sky)">$35</td><td style="background:var(--orange)">$30</td><td style="background:var(--sky)">$35</td>
    </tr>
  </table>
  <div class="ticks"></div>
</section>

<!-- Row 7 -->
<section class="slide" style="left:1px;top:842px">
  <div class="title" style="left:50px;top:8px;font-size:8px">Infographic <span class="hl">name</span></div>
  <div class="brand" style="right:6px;top:6px">Stroomwacht</div>
  <svg class="abs" style="left:0;top:0" width="222" height="125" viewBox="0 0 222 125" aria-hidden="true">
    <path d="M62 32H92L108 52H118" fill="none" stroke="var(--orange)" stroke-width="5"/>
    <path d="M62 62H118" fill="none" stroke="var(--blue)" stroke-width="5"/>
    <path d="M62 92H92L108 72H118" fill="none" stroke="var(--gold)" stroke-width="5"/>
    <circle cx="62" cy="32" r="5" fill="var(--orange)"/>
    <circle cx="62" cy="62" r="5" fill="var(--blue)"/>
    <circle cx="62" cy="92" r="5" fill="var(--gold)"/>
    <path d="M140 50H158L166 62L158 74H140Z" fill="var(--navy)"/>
    <path d="M160 50H166L174 62L166 74H160L168 62Z" fill="var(--navy)"/>
    <circle cx="128" cy="62" r="15" fill="var(--paper)" stroke="var(--navy)" stroke-width="1.5"/>
    <use href="#i-globe" x="118" y="52" width="20" height="20" color="var(--navy)"/>
  </svg>
  <div class="copy" style="left:14px;top:30px;width:34px">ICON 1<br>The point of using it</div>
  <div class="copy" style="left:14px;top:60px;width:34px">ICON 2<br>The point of using it</div>
  <div class="copy" style="left:14px;top:90px;width:34px">ICON 3<br>The point of using it</div>
  <div class="copy" style="left:178px;top:55px;width:32px">Why do we use it? The point of using data</div>
  <div class="ticks"></div>
</section>

<section class="slide" style="left:491px;top:842px">
  <div class="title" style="left:90px;top:8px;font-size:8px">Infographic <span class="hl">name</span></div>
  <div class="brand" style="right:6px;top:6px">Stroomwacht</div>
  <svg class="abs" style="left:0;top:0" width="222" height="125" viewBox="0 0 222 125" aria-hidden="true">
    <path d="M105 38V60H62V92" fill="none" stroke="var(--orange)" stroke-width="2.5"/>
    <path d="M110 38V70H80V96" fill="none" stroke="var(--grey)" stroke-width="2.5"/>
    <path d="M115 38V70H150V96" fill="none" stroke="var(--blue)" stroke-width="2.5"/>
    <path d="M120 38V55H172V70" fill="none" stroke="var(--gold)" stroke-width="2.5"/>
    <circle cx="112" cy="31" r="8" fill="var(--blue)"/>
    <use href="#i-home" x="106" y="25" width="12" height="12" color="#fff"/>
    <circle cx="62" cy="96" r="6" fill="var(--orange)"/>
    <circle cx="80" cy="96" r="6" fill="var(--grey)"/>
    <circle cx="150" cy="96" r="6" fill="var(--blue)"/>
    <circle cx="172" cy="70" r="6" fill="var(--gold)"/>
  </svg>
  <div class="tiny" style="left:98px;top:18px">Lorem ipsum</div>
  <div class="tiny" style="left:40px;top:58px">Lorem ipsum</div>
  <div class="tiny" style="left:180px;top:68px">Lorem ipsum</div>
  <div class="tiny" style="left:70px;top:104px">Lorem ipsum</div>
  <div class="tiny" style="left:138px;top:104px">Lorem ipsum</div>
  <div class="bar-orange"></div>
</section>

<!-- Row 8 -->
<section class="slide" style="left:128px;top:1003px">
  <div class="abs" style="left:0;top:88px;width:222px;height:37px;background:var(--orange)"></div>
  <div class="title" style="left:80px;top:8px;font-size:8px">Infographic <span class="hl">name</span></div>
  <div class="brand" style="right:6px;top:6px">Stroomwacht</div>
  <div class="device" style="left:84px;top:22px;width:54px;height:76px" role="img" aria-label="Tablet mockup"></div>
  <div class="tiny" style="left:24px;top:30px">Lorem ipsum</div><div class="icon-dot" style="left:58px;top:28px;color:#fff"><svg><use href="#i-doc"/></svg></div>
  <div class="tiny" style="left:24px;top:58px">Lorem ipsum</div><div class="icon-dot" style="left:58px;top:56px;color:#fff"><svg><use href="#i-gear"/></svg></div>
  <div class="tiny" style="left:24px;top:102px;color:#fff">Lorem ipsum</div><div class="icon-dot" style="left:58px;top:100px;background:#fff;color:var(--orange)"><svg><use href="#i-bolt"/></svg></div>
  <div class="icon-dot" style="left:155px;top:28px;color:#fff"><svg><use href="#i-doc"/></svg></div><div class="tiny" style="left:168px;top:30px">Lorem ipsum</div>
  <div class="icon-dot" style="left:155px;top:56px;color:#fff"><svg><use href="#i-eye"/></svg></div><div class="tiny" style="left:168px;top:58px">Lorem ipsum</div>
  <div class="icon-dot" style="left:155px;top:100px;background:#fff;color:var(--orange)"><svg><use href="#i-gear"/></svg></div><div class="tiny" style="left:168px;top:102px;color:#fff">Lorem ipsum</div>
  <div class="ticks"></div>
</section>

<section class="slide" style="left:369px;top:1003px">
  <svg class="abs" style="left:0;top:0" width="222" height="125" viewBox="0 0 222 125" aria-hidden="true">
    <path d="M120 0H222V125H150Q110 60 120 0Z" fill="var(--navy)"/>
  </svg>
  <div class="title" style="left:12px;top:8px;font-size:8px">Infographic <span class="hl">name</span></div>
  <div class="brand light" style="right:6px;top:6px">Stroomwacht</div>
  <div class="device" style="left:28px;top:30px;width:92px;height:60px;border-width:3px 3px 6px" role="img" aria-label="Laptop mockup"></div>
  <div class="icon-dot" style="left:150px;top:30px;background:#fff;color:var(--navy)"><svg><use href="#i-doc"/></svg></div><div class="tiny" style="left:163px;top:32px;color:#fff">Lorem ipsum</div>
  <div class="icon-dot" style="left:150px;top:58px;background:#fff;color:var(--navy)"><svg><use href="#i-bolt"/></svg></div><div class="tiny" style="left:163px;top:60px;color:#fff">Lorem ipsum</div>
  <div class="icon-dot" style="left:150px;top:86px;background:#fff;color:var(--navy)"><svg><use href="#i-gear"/></svg></div><div class="tiny" style="left:163px;top:88px;color:#fff">Lorem ipsum</div>
  <div class="ticks light"></div>
</section>

</body>
</html>
```